TALL WAVE

I am in this industry for last 15 years we have done lots of commercial site like we work with ORBEL costruction, loam properties, DRV, quill construction.
We do all domestic and commercial wall and floor tiling, swimming pools, spas, paving, marbles blue stones and muchmore.

Specializing in the wall and floor Tiling, Waterproofing and floor preparations

Industry/Entity Type

Industry

Number of Pages Required

1 page

Font styles to use
Serif
Decorative

Colors

Designer to choose colors to be used in the design.

Requirements
Must have
• domestic and commercial indoor tiling, bathroom tiling and paving pictures
Nice to have
• beautiful bathroom pictures with tile

```html
<!DOCTYPE html>
<html lang="en">
<head>
<meta charset="utf-8">
<title>Tall Wave — Wall &amp; Floor Tiling</title>
<link href="https://fonts.googleapis.com/css2?family=Cinzel:wght@400;700&family=Open+Sans:wght@400;600;700&display=swap" rel="stylesheet">
<style>
:root{
  --plum:#6a4a6c;
  --plum-dark:#5b3d5d;
  --ink:#2b2b2b;
  --text:#444;
  --muted:#777;
  --pale:#eef1f8;
  --white:#fff;
  --line:#d9dbe3;
}
*{box-sizing:border-box;margin:0;padding:0}
html,body{width:1200px;height:3822px;overflow:hidden}
body{position:relative;background:var(--white);font-family:"Open Sans",Arial,sans-serif;color:var(--text)}
.abs{position:absolute}
.heading{font-family:"Cinzel",Georgia,serif;color:var(--plum);font-weight:400;letter-spacing:2px;text-transform:uppercase}

/* hero */
.hero{left:0;top:0;width:1200px;height:637px;background:linear-gradient(100deg,#2d3552 0%,#4b5778 35%,#6d7590 55%,#3a4360 80%,#566282 100%)}
.brand{font-family:"Open Sans",Arial,sans-serif;font-weight:700;color:var(--white);letter-spacing:1px}
.hero-brand{left:171px;top:30px;font-size:24px}
.nav-projects{left:918px;top:34px;color:var(--white);font-size:14px;font-weight:700;letter-spacing:1px;display:flex;align-items:center;gap:10px}
.burger{width:30px;height:16px;border-top:2px solid #fff;border-bottom:2px solid #fff;position:relative}
.burger::after{content:"";position:absolute;left:0;right:0;top:5px;border-top:2px solid #fff}
.hero-title{left:555px;top:375px;font-family:"Cinzel",Georgia,serif;font-weight:400;color:var(--white);font-size:64px;line-height:78px;letter-spacing:5px}
.tabs{left:0;top:637px;width:1200px;height:38px;display:flex}
.tab{flex:0 0 601px;display:flex;align-items:center;justify-content:center;color:var(--white);font-size:13px;font-weight:700;letter-spacing:.5px}
.tab--res{background:var(--plum)}
.tab--com{flex:1;background:#2a2a2a}

/* services */
.services{left:0;top:675px;width:1200px;height:782px;background:linear-gradient(180deg,#ffffff 0%,#f1f4fa 30%,#cfd6e6 55%,#e7ebf3 75%,#f3f5f9 100%)}
.section-title{width:1200px;left:0;text-align:center;font-size:30px}
.intro{left:200px;top:830px;width:800px;text-align:center;font-size:12px;line-height:19px;color:var(--text)}
.card{width:272px;height:278px;top:991px;background:var(--white);box-shadow:0 2px 8px rgba(0,0,0,.08)}
.card .photo{height:168px}
.card h3{font-family:"Cinzel",Georgia,serif;font-weight:400;font-size:18px;color:var(--ink);text-align:center;margin-top:22px;letter-spacing:1px;text-transform:uppercase}
.card p{font-size:12px;line-height:17px;text-align:center;margin:12px 18px 0;color:var(--text)}
.arrow{top:1114px;width:16px;height:30px}

/* about */
.about-photo{left:466px;top:1541px;width:734px;height:459px;background:linear-gradient(160deg,#e9eef5 0%,#aac3e0 35%,#4d74a8 55%,#dfe6ef 80%,#c7d2e0 100%)}
.about-card{left:155px;top:1636px;width:523px;height:326px;background:rgba(255,255,255,.96);box-shadow:0 3px 14px rgba(0,0,0,.1);padding:60px 20px 0 20px}
.about-card h2{font-size:28px}
.about-card p{font-size:12.5px;line-height:19px;margin-top:30px;color:var(--text)}
.cta{display:inline-block;margin-top:40px;font-size:12px;font-weight:700;color:var(--plum);letter-spacing:.5px}

/* portfolio */
.filters{left:196px;top:2162px;width:808px;display:flex;justify-content:space-between;font-size:12.5px;color:var(--ink);border-bottom:1px solid var(--line);border-top:1px solid var(--line);padding:8px 8px}
.filters .active{position:relative}
.filters .active::after{content:"";position:absolute;left:50%;bottom:-14px;margin-left:-5px;border:5px solid transparent;border-bottom-color:var(--line)}
.tile{width:283px}

/* blog */
.blog{left:0;top:2821px;width:1200px;height:657px;background:var(--pale)}
.post{width:418px;height:188px;background:var(--white)}
.post .thumb{position:absolute;top:0;width:209px;height:188px}
.post .body{position:absolute;top:0;width:209px;padding:16px 14px}
.post h4{font-family:"Cinzel",Georgia,serif;font-weight:400;font-size:15px;line-height:20px;color:var(--plum);letter-spacing:1px;text-transform:uppercase}
.post p{font-size:12px;line-height:17px;margin-top:12px;color:var(--text)}
.post .meta{font-size:11.5px;margin-top:14px;color:var(--text)}
.read-more{left:0;width:1200px;top:3412px;text-align:center;font-size:12px;font-weight:700;color:var(--ink);letter-spacing:.5px}

/* footer */
.footer{left:0;top:3478px;width:1200px;height:344px;background:var(--plum-dark)}
.footer .brand{left:0;width:1200px;top:80px;text-align:center;font-size:28px}
.footer-rule{left:171px;top:173px;width:858px;border-top:1px solid rgba(255,255,255,.25)}
.socials{left:0;width:1200px;top:202px;display:flex;justify-content:center;gap:26px}
.social{width:34px;height:34px;border:1px solid rgba(255,255,255,.6);border-radius:50%;display:flex;align-items:center;justify-content:center}
.social svg{width:14px;height:14px}
.copyright{left:0;width:1200px;top:268px;text-align:center;color:var(--white);font-size:12px}
.top-tab{left:570px;top:3792px;width:60px;height:30px}
</style>
</head>
<body>

<!-- Hero -->
<section class="abs hero" role="img" aria-label="Modern bathroom with dark blue wall tiles, glass shower and white vanity"></section>
<div class="abs brand hero-brand">Tall Wave</div>
<div class="abs nav-projects">PROJECTS <span class="burger"></span></div>
<h1 class="abs hero-title">Feel the<br>Awesomeness</h1>
<nav class="abs tabs">
  <div class="tab tab--res">RESIDENCIAL WORKS</div>
  <div class="tab tab--com">COMMERTIAL WORKS</div>
</nav>

<!-- Services -->
<section class="abs services" role="img" aria-label="Soft background of a bright white tiled bathroom"></section>
<h2 class="abs heading section-title" style="top:762px">Our Professional Services</h2>
<p class="abs intro">Sed ut perspiciatis unde omnis iste natus error sit voluptatem accusantium doloremque laudantium, totam rem aperiam,<br>eaque ipsa quae ab illo inventore<br>veritatis et quasi architecto beatae vitae dicta sunt explicabo. Nemo enim ipsam voluptatem quia voluptas sit aspernatur<br>et dolorum fuga. Et harum quidem rerum facilis est et expedita distinctio.</p>

<svg class="abs arrow" style="left:132px" viewBox="0 0 16 30"><polyline points="12,2 4,15 12,28" fill="none" stroke="#555" stroke-width="1.5"/></svg>
<svg class="abs arrow" style="left:1054px" viewBox="0 0 16 30"><polyline points="4,2 12,15 4,28" fill="none" stroke="#555" stroke-width="1.5"/></svg>

<article class="abs card" style="left:171px">
  <div class="photo" role="img" aria-label="Bathroom with purple wall tiles and glossy floor tiling" style="background:linear-gradient(135deg,#7d4a78 0%,#c79ab8 50%,#3d2a3c 100%)"></div>
  <h3>Wall &amp; Floor Tiling</h3>
  <p>Veritatis et quasi architecto beatae vitae dicta sunt explicabo emo enim ipsam</p>
</article>
<article class="abs card" style="left:466px">
  <div class="photo" role="img" aria-label="Blue waterproofing membrane applied to a wet area" style="background:linear-gradient(135deg,#8a7a66 0%,#2e5fae 55%,#6a7d9a 100%)"></div>
  <h3>Waterproofing</h3>
  <p>Architecto beatae vitae dicta sunt expl icabo. Nemo enim ipsam vol uptatem</p>
</article>
<article class="abs card" style="left:759px">
  <div class="photo" role="img" aria-label="Workers grinding and levelling a concrete floor" style="background:linear-gradient(135deg,#3b4a5a 0%,#8fa0b2 55%,#5a6470 100%)"></div>
  <h3>Floor Preparations</h3>
  <p>Quasi architecto beatae vitae dicta sunt explicabo emo enim ipsam vol uptatem</p>
</article>

<!-- About -->
<svg class="abs" style="left:0;top:1457px" width="1200" height="700" viewBox="0 0 1200 700" aria-hidden="true">
  <polygon points="0,500 1200,280 1200,700 0,700" fill="#e6ebf5"/>
  <polygon points="0,640 1200,560 1200,700 0,700" fill="#ffffff"/>
</svg>
<div class="abs about-photo" role="img" aria-label="White kitchen with sky-printed glass splashback and cabinet fronts"></div>
<section class="abs about-card">
  <h2 class="heading">About Us</h2>
  <p>Sed ut perspiciatis unde omnis iste natus error sit voluptatem accusantium dol omque laudantium, totam rem aperiam, eaque ipsa quae Sed ut perspiciatis unde omnis iste natus error sit voluptatem accusantium doloremque laudantium, totam rem aperiam. Totam rem aperiam, eaque ipsa quae Sed ut perspiciatis unde omnis iste natus error sit voluptatem rem aperiam.</p>
  <span class="cta">GET STARTED &nbsp;&rsaquo;</span>
</section>

<!-- Portfolio -->
<h2 class="abs heading section-title" style="top:2090px">Our Professional Services</h2>
<nav class="abs filters">
  <span class="active">All</span><span>Wall and floor Tiling</span><span>Waterproofing</span><span>Floor preparations</span><span>Swimming pools</span><span>Spas</span><span>Paving</span><span>Marbles blue stones</span>
</nav>
<div class="abs tile" style="left:171px;top:2229px;height:173px;background:linear-gradient(135deg,#d9d2c4,#b89a7a 60%,#efe9dc)" role="img" aria-label="Living room feature wall with mosaic tiles"></div>
<div class="abs tile" style="left:459px;top:2229px;height:173px;background:linear-gradient(135deg,#2f6d9a,#7fb3d4 50%,#3c5f7a)" role="img" aria-label="Pool edge with stone coping and water"></div>
<div class="abs tile" style="left:747px;top:2229px;height:351px;background:linear-gradient(160deg,#cbb89a,#e7dcc7 45%,#4b9a9a 80%,#7a6a55)" role="img" aria-label="Arched tiled spa room with round plunge pool"></div>
<div class="abs tile" style="left:171px;top:2409px;height:171px;background:linear-gradient(180deg,#5c7696,#8aa2bd)" role="img" aria-label="Blue painted wall with pendant lights"></div>
<div class="abs tile" style="left:459px;top:2409px;height:171px;background:linear-gradient(135deg,#b9a58c,#dccbb4 60%,#8c7864)" role="img" aria-label="Beige porcelain floor tiles being laid"></div>
<div class="abs tile" style="left:171px;top:2588px;height:177px;background:linear-gradient(180deg,#2c5f99,#7ea6cf 45%,#f3f4f6 70%)" role="img" aria-label="Kitchen with blue subway tile splashback"></div>
<div class="abs tile" style="left:459px;top:2588px;height:177px;background:linear-gradient(180deg,#4f6a3a,#7f9a62 35%,#3d9ad1 70%,#8a7a66)" role="img" aria-label="Outdoor swimming pool with paved surround"></div>
<div class="abs tile" style="left:747px;top:2588px;height:177px;background:linear-gradient(135deg,#f2eee8,#d8cdbf 55%,#7a5a40)" role="img" aria-label="Marble floor tiles in a bright open room"></div>

<!-- Blog -->
<section class="abs blog"></section>
<h2 class="abs heading section-title" style="top:2872px">Recent From Blogs</h2>

<article class="abs post" style="left:171px;top:2948px">
  <div class="thumb" style="left:0;background:linear-gradient(180deg,#6e8a5a,#3fa6cf 60%,#2f7fae)" role="img" aria-label="Tiled pool edge with waterfall feature"></div>
  <div class="body" style="left:209px"><h4>Lorem ipsum dolor sit amet</h4><p>Sed ut perspiciatis unde omnis iste natus error sit volupt[...]</p><div class="meta">By Admin , 25th June</div></div>
</article>
<article class="abs post" style="left:612px;top:2948px">
  <div class="thumb" style="left:0;background:linear-gradient(135deg,#d6d6d6,#8e8e8e 55%,#eaeaea)" role="img" aria-label="Tiler pressing a floor tile into adhesive"></div>
  <div class="body" style="left:209px"><h4>Lorem ipsum dolor sit amet</h4><p>Sed ut perspiciatis unde omnis iste natus error sit volupt[...]</p><div class="meta">By Admin , 25th June</div></div>
</article>
<article class="abs post" style="left:171px;top:3165px">
  <div class="body" style="left:0"><h4>Lorem ipsum dolor sit amet</h4><p>Sed ut perspiciatis unde omnis iste natus error sit volupt[...]</p><div class="meta">By Admin , 25th June</div></div>
  <div class="thumb" style="left:209px;background:linear-gradient(135deg,#cdbfa8,#8f7a62 55%,#e6ddcf)" role="img" aria-label="Stone feature wall with vases"></div>
</article>
<article class="abs post" style="left:612px;top:3165px">
  <div class="body" style="left:0"><h4>Lorem ipsum dolor sit amet</h4><p>Sed ut perspiciatis unde omnis iste natus error sit volupt[...]</p><div class="meta">By Admin , 25th June</div></div>
  <div class="thumb" style="left:209px;background:linear-gradient(135deg,#f1f1f1,#cfd2d6 60%,#ffffff)" role="img" aria-label="White bathroom basin against hexagon wall tiles"></div>
</article>
<div class="abs read-more">READ MORE &nbsp;&rsaquo;</div>

<!-- Footer -->
<footer class="abs footer">
  <div class="abs brand">Tall Wave</div>
  <div class="abs footer-rule"></div>
  <div class="abs socials">
    <span class="social" aria-label="Share"><svg viewBox="0 0 14 14"><circle cx="3" cy="7" r="1.8" fill="#fff"/><circle cx="11" cy="3" r="1.8" fill="#fff"/><circle cx="11" cy="11" r="1.8" fill="#fff"/><path d="M3 7L11 3M3 7L11 11" stroke="#fff" stroke-width="1.1"/></svg></span>
    <span class="social" aria-label="Message"><svg viewBox="0 0 14 14"><path d="M2 3h10v6H6l-3 3V9H2z" fill="none" stroke="#fff" stroke-width="1.3" stroke-linejoin="round"/></svg></span>
    <span class="social" aria-label="Website"><svg viewBox="0 0 14 14"><circle cx="7" cy="7" r="5.3" fill="none" stroke="#fff" stroke-width="1.2"/><ellipse cx="7" cy="7" rx="2.3" ry="5.3" fill="none" stroke="#fff" stroke-width="1"/><path d="M1.7 7h10.6" stroke="#fff" stroke-width="1"/></svg></span>
  </div>
  <div class="abs copyright">Copyright © Tall Wave 2017</div>
</footer>
<svg class="abs top-tab" viewBox="0 0 60 30" aria-label="Back to top">
  <polygon points="0,30 30,0 60,30" fill="#fff"/>
  <polyline points="22,24 30,16 38,24" fill="none" stroke="#333" stroke-width="2"/>
</svg>

</body>
</html>
```